Business cards for investing fund

I need processional luxury classical business cards for CEO of the investing company. I need it to be elegant. I need it to look expensive. It will be printed o fine paper with UV. I prefer light and minimalistic design. Logo of my company must be included at least on front page.

Target Market(s)

40+ investors

Industry/Entity Type

Finance And Accounting

Contact Information for Business Card

FRONT PAGE:

Bartosz Wielka
President & CEO

e: bart@kpfvc.com
w: www.kpfvc.com
p: +44 20 8672 3915
m: +44 73 9185 2247

Kite Perch Fern Venture Capital, LLC
47 W Larkin St., Sheridan, WY 82801
Filling number: 2019-000431952

BACK PAGE (with or without logo):

PROUD GROUP MEMBERS:

UK: Marlow Brook Associates Ltd. | 62 Little Ashford St., 1st fl. | W1K-3PQ London
PL: Marlow Brook Trust S.A. | R17 ul. Okrężna 14, 3p. | 00-418 Warszawa
US: Nine Cobalt Advisors, LLC | 731 Ninth Avenue, Suite 402, NYC | 10019 New York

Font styles to use
Serif
Sans Serif
Decorative

Colors
0355a3
ec1f27

Requirements
Must have
• My own logo (attached)

```html
<!DOCTYPE html>
<html lang="en">
<head>
<meta charset="utf-8">
<title>Kite Perch Fern Venture Capital — Business Cards</title>
<link rel="stylesheet" href="https://fonts.googleapis.com/css2?family=Josefin+Slab:wght@400;600&display=swap">
<style>
  :root {
    --brand-blue: #0355a3;
    --brand-red: #ec1f27;
    --ink: #3a3a3a;
    --stage: #77787b;
    --card: #ffffff;
    --rule-dark: #4a4a4a;
  }
  * { margin: 0; padding: 0; box-sizing: border-box; }
  html, body { width: 1200px; height: 1200px; overflow: hidden; }
  body {
    background: var(--stage);
    font-family: "Josefin Slab", Georgia, serif;
    font-weight: 600;
    color: var(--ink);
    position: relative;
  }
  .card {
    position: absolute;
    top: 226px;
    width: 427px;
    height: 748px;
    background: var(--card);
    overflow: hidden;
  }
  .card--front { left: 119px; }
  .card--back { left: 649px; }
  .card * { position: absolute; line-height: 1; white-space: nowrap; }

  .card__bar { left: 0; bottom: 0; width: 100%; height: 6px; background: var(--rule-dark); }
  .card__bar::before { content: ""; position: absolute; left: 0; top: 0; width: 50%; height: 100%; background: var(--brand-blue); }

  /* Company name set plainly in the text face */
  .company-name { color: var(--brand-blue); font-weight: 600; letter-spacing: 0.5px; }
  .company-name__square { width: 14px; height: 14px; background: var(--brand-blue); }
  .company-name__text { position: absolute; white-space: normal; line-height: 1.2; }

  .front-name .company-name__square { left: 39px; top: 50px; }
  .front-name .company-name__text { left: 39px; top: 82px; width: 300px; font-size: 32px; }

  .back-name .company-name__square { right: 51px; top: 46px; }
  .back-name .company-name__text { right: 51px; top: 72px; width: 220px; font-size: 20px; text-align: right; }

  .dash { width: 22px; height: 2px; background: var(--brand-blue); }
  .card--front .dash { left: 39px; top: 302px; }

  .holder-name { left: 39px; top: 353px; font-size: 26px; color: var(--brand-blue); letter-spacing: 1px; }
  .holder-role { left: 39px; top: 382px; font-size: 21px; }

  .contact { left: 0; width: 210px; text-align: right; font-size: 21px; }
  .contact-icon { left: 228px; width: 22px; height: 22px; }
  .contact-icon svg { position: static; display: block; }

  .filing { left: 39px; top: 656px; font-size: 21px; }
  .address { left: 39px; top: 687px; font-size: 21px; color: var(--brand-blue); }

  .card--back .dash { right: 51px; top: 194px; }
  .members-title { right: 51px; top: 216px; font-size: 22px; letter-spacing: 1.5px; }
  .flag { right: 51px; width: 24px; height: 24px; }
  .flag svg { position: static; display: block; }
  .member { right: 51px; text-align: right; font-size: 21px; }
  .member--name { color: var(--brand-blue); }
</style>
</head>
<body>

<section class="card card--front" aria-label="Business card front">
  <div class="company-name front-name">
    <span class="company-name__square"></span>
    <p class="company-name__text">Kite Perch Fern Venture Capital, LLC</p>
  </div>

  <div class="dash"></div>

  <p class="holder-name">BARTOSZ WIELKA</p>
  <p class="holder-role">President &amp; CEO</p>

  <p class="contact" style="top:470px">+44 20 8672 3915</p>
  <div class="contact-icon" style="top:469px">
    <svg width="22" height="22" viewBox="0 0 24 24" fill="none" stroke="#0355a3" stroke-width="1.6" stroke-linecap="round"><path d="M5 3h3l2 5-2 1.5a11 11 0 0 0 6.5 6.5L16 14l5 2v3a2 2 0 0 1-2 2A17 17 0 0 1 3 5a2 2 0 0 1 2-2z"/><path d="M14 3a7 7 0 0 1 7 7M14 7a3 3 0 0 1 3 3"/></svg>
  </div>

  <p class="contact" style="top:500px">+44 73 9185 2247</p>
  <div class="contact-icon" style="top:499px">
    <svg width="22" height="22" viewBox="0 0 24 24" fill="none" stroke="#0355a3" stroke-width="1.8"><rect x="7" y="2.5" width="10" height="19" rx="1.5"/><path d="M10.5 18h3"/></svg>
  </div>

  <p class="contact" style="top:531px">bart@kpfvc.com</p>
  <div class="contact-icon" style="top:530px">
    <svg width="22" height="22" viewBox="0 0 24 24" fill="none" stroke="#0355a3" stroke-width="1.6"><rect x="2.5" y="5" width="19" height="14" rx="1"/><path d="M3 6l9 7 9-7"/></svg>
  </div>

  <p class="contact" style="top:561px">www.kpfvc.com</p>
  <div class="contact-icon" style="top:560px">
    <svg width="22" height="22" viewBox="0 0 24 24" fill="none" stroke="#0355a3" stroke-width="1.6"><circle cx="12" cy="12" r="9.5"/><ellipse cx="12" cy="12" rx="4.5" ry="9.5"/><path d="M2.5 12h19M4 7h16M4 17h16"/></svg>
  </div>

  <p class="filing">2019-000431952</p>
  <p class="address">47 W Larkin St. Sheridan, WY 82801</p>

  <div class="card__bar"></div>
</section>

<section class="card card--back" aria-label="Business card back">
  <div class="company-name back-name">
    <span class="company-name__square"></span>
    <p class="company-name__text">Kite Perch Fern Venture Capital, LLC</p>
  </div>

  <div class="dash"></div>
  <p class="members-title">PROUD GROUP MEMBERS</p>

  <div class="flag" style="top:263px" aria-label="United Kingdom">
    <svg width="24" height="24" viewBox="0 0 24 24"><circle cx="12" cy="12" r="11.5" fill="#fff"/><path d="M10 1h4v22h-4zM1 10h22v4H1z" fill="#ec1f27"/></svg>
  </div>
  <p class="member member--name" style="top:314px">Marlow Brook Associates Ltd.</p>
  <p class="member" style="top:344px">62 Little Ashford St. 1st fl.</p>
  <p class="member" style="top:375px">W1K-3PQ London</p>

  <div class="flag" style="top:422px" aria-label="Poland">
    <svg width="24" height="24" viewBox="0 0 24 24"><clipPath id="pl"><circle cx="12" cy="12" r="11.5"/></clipPath><g clip-path="url(#pl)"><rect width="24" height="12" fill="#f2f2f2"/><rect y="12" width="24" height="12" fill="#ec1f27"/></g></svg>
  </div>
  <p class="member member--name" style="top:470px">Marlow Brook Trust S.A.</p>
  <p class="member" style="top:500px">R17 ul. Okrężna 14, 3p.</p>
  <p class="member" style="top:531px">00-418 Warszawa</p>

  <div class="flag" style="top:577px" aria-label="United States">
    <svg width="24" height="24" viewBox="0 0 24 24"><clipPath id="us"><circle cx="12" cy="12" r="11.5"/></clipPath><g clip-path="url(#us)"><rect width="24" height="24" fill="#fff"/><g fill="#ec1f27"><rect y="0" width="24" height="2"/><rect y="4" width="24" height="2"/><rect y="8" width="24" height="2"/><rect y="12" width="24" height="2"/><rect y="16" width="24" height="2"/><rect y="20" width="24" height="2"/></g><rect width="11" height="11" fill="#0355a3"/></g></svg>
  </div>
  <p class="member member--name" style="top:625px">Nine Cobalt Advisors, LLC</p>
  <p class="member" style="top:655px">731 Ninth Avenue, Suite 402, NYC</p>
  <p class="member" style="top:686px">10019 New York</p>

  <div class="card__bar"></div>
</section>

</body>
</html>
```